Meridian Sound Wellness LLC Card Design

Need business card with a logo for a hearing aid sales and audiology business. We have two Hearing Instrument Specialists and one Audiologist on staff. Over 25 years in business. Locally owned and operated. Financing available. Most insurances accepted.

Meridian Sound Wellness LLC
48730 W Linden Row, Suite 9
Spokane, WA 99481
509-617-2085
www.meridiansoundnorth.example

Manager
Tobias Wrenfield HIS COHC
License #81729046

Target Market(s)

50yr old + people with a hearing loss.

Industry/Entity Type

Business

Contact Information for Business Card

48730 W Linden Row, Suite 9
Spokane, WA 99481
509-617-2085
www.meridiansoundnorth.example

Manager
Tobias Wrenfield HIS COHC
NRPL #81729046

Font styles to use
Serif
Sans Serif

Requirements
Must have
• Business name, Tobias's name and title(s) and contact information, License #, web address
Nice to have
Should not have

```html
<!DOCTYPE html>
<html lang="en">
<head>
<meta charset="utf-8">
<title>Meridian Sound Wellness LLC – Business Card</title>
<link rel="stylesheet" href="https://fonts.googleapis.com/css2?family=Ubuntu:wght@400;500&display=swap">
<style>
  :root {
    --page: #ecebe7;
    --card: #ffffff;
    --blue: #5a8dc3;
    --blue-text: #3f74b3;
    --green: #9bcb55;
    --orange: #eb9a2a;
    --white: #ffffff;
  }
  html, body {
    margin: 0;
    width: 1200px;
    height: 1022px;
    overflow: hidden;
    background: var(--page);
    font-family: "Ubuntu", "Trebuchet MS", sans-serif;
  }
  .card {
    position: absolute;
    left: 100px;
    top: 225px;
    width: 1000px;
    height: 572px;
    background: var(--card);
    box-shadow: 0 10px 30px rgba(0,0,0,0.18);
    overflow: hidden;
  }
  .bands {
    position: absolute;
    left: 0;
    top: 0;
  }
  .brand {
    position: absolute;
    left: 70px;
    top: 140px;
    display: flex;
    align-items: center;
    gap: 26px;
  }
  .brand-dot {
    width: 70px;
    height: 70px;
    border-radius: 50%;
    background: var(--orange);
    flex: none;
  }
  .brand-name {
    color: var(--blue-text);
    font-size: 44px;
    font-weight: 400;
    line-height: 1.1;
  }
  .person {
    position: absolute;
    right: 40px;
    top: 60px;
    text-align: right;
  }
  .person-name {
    display: flex;
    align-items: center;
    justify-content: flex-end;
    gap: 12px;
    color: var(--blue-text);
    font-size: 34px;
  }
  .person-icon { width: 40px; height: 40px; }
  .person-title {
    color: var(--orange);
    font-size: 28px;
    margin: 6px 52px 0 0;
  }
  .person-license {
    color: var(--green);
    font-size: 24px;
    margin: 4px 52px 0 0;
  }
  .contact {
    position: absolute;
    left: 300px;
    top: 474px;
    margin: 0;
    padding: 0;
    list-style: none;
    color: var(--white);
    font-size: 21px;
  }
  .contact li {
    display: flex;
    align-items: center;
    gap: 12px;
    height: 31px;
  }
  .contact svg { width: 22px; height: 22px; flex: none; }
  .address {
    position: absolute;
    right: 30px;
    top: 372px;
    text-align: right;
    color: var(--white);
    font-size: 22px;
    font-style: normal;
    line-height: 1.35;
  }
</style>
</head>
<body>
  <main class="card">
    <svg class="bands" width="1000" height="572" viewBox="0 0 1000 572" aria-hidden="true">
      <polygon class="band-green" points="770,350 1000,350 1000,572 700,572" fill="var(--green)"/>
      <polygon class="band-blue" points="285,460 780,460 735,572 250,572" fill="var(--blue)"/>
    </svg>

    <div class="brand">
      <span class="brand-dot"></span>
      <div class="brand-name">Meridian Sound<br>Wellness LLC</div>
    </div>

    <div class="person">
      <div class="person-name">
        Tobias Wrenfield HIS COHC
        <svg class="person-icon" viewBox="0 0 40 40" aria-hidden="true">
          <circle cx="20" cy="20" r="20" fill="var(--orange)"/>
          <circle cx="20" cy="14" r="6" fill="#fff"/>
          <path d="M9 31 a11 10 0 0 1 22 0 z" fill="#fff"/>
        </svg>
      </div>
      <div class="person-title">Manager</div>
      <div class="person-license">NRPL #81729046</div>
    </div>

    <ul class="contact">
      <li>
        <svg viewBox="0 0 26 26" aria-hidden="true">
          <circle cx="13" cy="13" r="13" fill="var(--green)"/>
          <path d="M8 7 l3 -1 l2 4 l-2 1.5 a8 8 0 0 0 4 4 l1.5 -2 l4 2 l-1 3 c-7 0 -11.5 -4.5 -11.5 -11.5z" fill="#fff"/>
        </svg>
        509-617-2085
      </li>
      <li>
        <svg viewBox="0 0 26 26" aria-hidden="true">
          <rect x="3" y="7" width="20" height="13" fill="var(--green)"/>
          <path d="M3 7 l10 8 l10 -8" fill="none" stroke="#fff" stroke-width="2"/>
        </svg>
        hello@meridiansound.example
      </li>
      <li>
        <svg viewBox="0 0 26 26" aria-hidden="true">
          <circle cx="13" cy="13" r="11" fill="var(--green)"/>
          <g fill="none" stroke="#fff" stroke-width="1.5">
            <ellipse cx="13" cy="13" rx="5" ry="11"/>
            <line x1="2" y1="13" x2="24" y2="13"/>
            <line x1="4" y1="8" x2="22" y2="8"/>
            <line x1="4" y1="18" x2="22" y2="18"/>
          </g>
        </svg>
        www.meridiansoundnorth.example
      </li>
    </ul>

    <address class="address">
      48730 W Linden Row<br>
      Suite 9<br>
      Spokane, WA 99481
    </address>
  </main>
</body>
</html>
```